BRINDLEWAVE is a New Zealand based aerial imaging company performing mapping, surveying and videography

I would like a business card that is contemporary and clean. The font for the business name is called Gtec Technology and I would like to have the text "AERIAL IMAGING" under the "BRINDLEWAVE" name in a font similar to URW Gothic or another light modern font. Brindlewave performs aerial imaging projects using a hexacopter UAV. Surveying and mapping with 3D Digital Elevation Models are a focus, I also produce aerial photographs and video's including post editing.
Updates

Target Market(s)

Industrial plant managers, Property owners, Event organisers.

Industry/Entity Type

Videography

Contact Information for Business Card

BRINDLEWAVE AERIAL IMAGING. Owner Ross Pellow. Cell: 027 4913068. P.O. Box 8321 Kelvale, Westmere.

Font styles to use
Other font styles liked:
• Gtec Technology

Colors
9bcb3b
33a6d7
ec1f27

Requirements
Must have
• Modern professional look.
Nice to have
• Perhaps an aerial image of a landscape who's location is not identifiable. Maybe use included image of my hexacopter on the back of the card? Not compulsory though.
Should not have
• Clip Art style images.

```html
<!DOCTYPE html>
<html lang="en">
<head>
<meta charset="utf-8">
<title>Brindlewave Aerial Imaging – Business Card</title>
<link rel="stylesheet" href="https://fonts.googleapis.com/css2?family=Orbitron:wght@500&family=Questrial&family=Oswald:wght@500&display=swap">
<style>
  :root {
    --ink: #0b0b0b;
    --paper-white: #ffffff;
    --brand-blue: #33a6d7;
    --brand-green: #9bcb3b;
    --brand-red: #ec1f27;
    --backdrop: #e9e6e8;
    --sky-pale: #dfeaf2;
    --land-green: #b9d68a;
    --water-blue: #a9cde3;
  }
  * { box-sizing: border-box; margin: 0; padding: 0; }
  html, body { width: 1200px; height: 800px; overflow: hidden; }
  body {
    background: var(--backdrop);
    display: flex;
    align-items: center;
    justify-content: center;
    gap: 40px;
  }
  .card {
    position: relative;
    width: 540px;
    height: 308px;
    overflow: hidden;
    box-shadow: 0 6px 18px rgba(0,0,0,0.18);
  }

  /* Reverse side */
  .card-back { background: var(--paper-white); }
  .landscape-photo {
    position: absolute;
    inset: 0;
    background:
      linear-gradient(160deg, var(--sky-pale) 0%, var(--sky-pale) 30%, transparent 45%),
      linear-gradient(100deg, var(--land-green) 0%, var(--water-blue) 45%, var(--land-green) 75%, #cfe3a6 100%);
  }
  .brand-band {
    position: absolute;
    left: 0; right: 0;
    top: 112px;
    height: 66px;
    background: var(--ink);
  }
  .brand-band .wordmark {
    position: absolute;
    left: 26px;
    top: 10px;
    font-size: 34px;
  }
  .brand-band .tagline {
    position: absolute;
    left: 210px;
    top: 44px;
    font-size: 15px;
  }

  /* Front side */
  .card-front { background: var(--ink); color: var(--paper-white); }
  .card-front .wordmark {
    position: absolute;
    left: 56px;
    top: 48px;
    font-size: 36px;
  }
  .card-front .tagline {
    position: absolute;
    left: 196px;
    top: 94px;
    font-size: 15px;
  }

  .wordmark {
    font-family: "Orbitron", sans-serif;
    font-weight: 500;
    letter-spacing: 3px;
    color: var(--paper-white);
    line-height: 1;
    white-space: nowrap;
  }
  .tagline {
    font-family: "Questrial", sans-serif;
    color: var(--brand-green);
    letter-spacing: 1px;
    line-height: 1;
    white-space: nowrap;
  }
  .owner-name {
    position: absolute;
    left: 150px;
    top: 142px;
    font-family: "Orbitron", sans-serif;
    font-weight: 500;
    font-size: 21px;
    letter-spacing: 1px;
    text-transform: uppercase;
    white-space: nowrap;
  }
  .contact-list {
    position: absolute;
    left: 118px;
    top: 196px;
    list-style: none;
    font-family: "Oswald", sans-serif;
    font-weight: 500;
    font-size: 15px;
    letter-spacing: 1px;
    white-space: nowrap;
  }
  .contact-item {
    display: flex;
    align-items: center;
    gap: 12px;
    height: 32px;
  }
  .contact-icon { width: 14px; height: 18px; fill: none; stroke: var(--paper-white); stroke-width: 1.6; }
  .contact-icon.filled { fill: var(--paper-white); stroke: none; }
</style>
</head>
<body>
  <section class="card card-back" aria-label="Business card reverse">
    <div class="landscape-photo" role="img" aria-label="Aerial landscape map with a hexacopter drone flying above"></div>
    <div class="brand-band">
      <div class="wordmark">BRINDLEWAVE</div>
      <div class="tagline">Aerial Imaging</div>
    </div>
  </section>

  <section class="card card-front" aria-label="Business card front">
    <div class="wordmark">BRINDLEWAVE</div>
    <div class="tagline">Aerial Imaging</div>
    <div class="owner-name">Ross Pellow</div>
    <ul class="contact-list">
      <li class="contact-item">
        <svg class="contact-icon" viewBox="0 0 14 18" aria-hidden="true">
          <rect x="2" y="1" width="10" height="16" rx="2"/>
          <line x1="5.5" y1="14" x2="8.5" y2="14"/>
        </svg>
        <span>027 4913068</span>
      </li>
      <li class="contact-item">
        <svg class="contact-icon filled" viewBox="0 0 14 18" aria-hidden="true">
          <path d="M7 0C3.1 0 0 3 0 6.8 0 11.5 7 18 7 18s7-6.5 7-11.2C14 3 10.9 0 7 0zm0 9.5A2.7 2.7 0 1 1 7 4a2.7 2.7 0 0 1 0 5.5z"/>
        </svg>
        <span>P.O. Box 8321 Kelvale, Westmere</span>
      </li>
    </ul>
  </section>
</body>
</html>
```